New Brochure Design Project | 8Fennox

We are looking for a new fresh brochure. The winner will help us build 2-3 more additional brochures. We attempted the basic content. Slides 5,6 and 7 are required from the powerpoint. The final should be created in Powerpoint so we can update on our own. I think we would like 1 page front and back with no fold if possible but if required. We are in the middle of redoing our website and have included the updated website and would like similar designs and colors.

Industry/Entity Type

Build

Requirements
Must have
• see project description for all details.

```html
<!DOCTYPE html>
<html lang="en">
<head>
<meta charset="utf-8">
<title>8Fennox Brochure</title>
<link href="https://fonts.googleapis.com/css2?family=Black+Ops+One&family=Open+Sans:wght@400;600;800&display=swap" rel="stylesheet">
<style>
:root{
  --red:#d8262b;
  --red-dark:#b71c22;
  --slate:#5f6b7a;
  --slate-dark:#4a5563;
  --charcoal:#3f4042;
  --paper:#e7e8ea;
  --stripe:#a3a9b1;
  --ink:#1c1c1e;
  --white:#ffffff;
  --stage:#d2d3d5;
}
*{margin:0;padding:0;box-sizing:border-box}
html,body{width:1200px;height:900px;overflow:hidden}
body{background:var(--stage);font-family:"Open Sans",sans-serif;position:relative}
.page{position:absolute;top:250px;width:580px;height:400px;background:var(--paper);overflow:hidden;box-shadow:0 2px 6px rgba(0,0,0,.18)}
.page--cover{left:10px}
.page--inside{left:610px}
.page__shapes{position:absolute;inset:0;width:100%;height:100%}
.display{font-family:"Black Ops One",sans-serif;text-transform:uppercase;line-height:1;white-space:nowrap}

/* cover */
.cover__brand{position:absolute;left:340px;top:12px;font-weight:800;font-size:40px;color:var(--paper);letter-spacing:1px}
.cover__label{position:absolute;left:330px;top:72px;font-size:22px;color:var(--red);text-decoration:underline;text-decoration-thickness:2px;text-underline-offset:3px}
.cover__line1{position:absolute;left:190px;top:140px;font-size:30px;color:var(--ink)}
.cover__line2{position:absolute;left:250px;top:180px;font-size:30px;color:var(--ink)}
.cover__line3{position:absolute;right:36px;top:226px;font-size:28px;color:var(--red)}
.slash-x{position:relative;display:inline-block}
.slash-x::after{content:"";position:absolute;left:50%;top:-12px;width:4px;height:54px;background:var(--red);transform:rotate(28deg);transform-origin:center}

/* footer shared */
.footer{position:absolute;left:0;right:0;bottom:0;height:56px}
.footer__top{position:absolute;right:0;top:0;height:26px;left:0;display:flex;justify-content:flex-end;align-items:center;gap:10px;padding-right:16px;font-size:7px;color:var(--white)}
.footer__bottom{position:absolute;left:0;right:0;bottom:0;height:30px;background:var(--slate-dark);display:flex;align-items:center;padding-left:22px;gap:10px;font-size:7px;color:#d9dde2}
.footer__name{position:absolute;left:205px;top:4px;font-weight:800;font-size:15px;line-height:18px;color:var(--red)}

/* inside */
.inside__title{position:absolute;left:110px;top:26px;font-size:26px;color:var(--white);letter-spacing:1px}
.inside__sub{position:absolute;right:28px;top:68px;width:190px;font-weight:800;font-size:9px;line-height:1.25;color:var(--white);text-align:right}
.cards{position:absolute;left:28px;right:28px;top:128px;display:flex;gap:8px}
.card{position:relative;flex:1;padding-top:26px}
.card__icon{position:absolute;top:0;left:50%;transform:translateX(-50%);width:20px;height:20px}
.card__box{position:relative;height:192px;background:var(--white);border:1px solid var(--charcoal);padding:38px 8px 8px}
.card__corner{position:absolute;left:-1px;top:-1px;width:40px;height:34px}
.card__title{position:absolute;left:34px;right:4px;top:5px;font-weight:800;font-size:7px;line-height:1.2;color:var(--ink);text-align:center}
.card__text{font-size:6.5px;line-height:1.45;color:#5a5d62;text-align:center;margin-bottom:8px}
</style>
</head>
<body>

<section class="page page--cover">
  <svg class="page__shapes" viewBox="0 0 580 400" aria-hidden="true">
    <polygon points="0,0 250,0 20,344 0,344" fill="var(--red)"/>
    <polygon points="250,0 266,0 36,344 20,344" fill="var(--stripe)"/>
    <polygon points="266,0 580,0 580,64 223,64" fill="var(--slate)"/>
    <rect x="300" y="100" width="280" height="3" fill="var(--red)"/>
    <rect x="0" y="344" width="580" height="26" fill="var(--slate)"/>
  </svg>
  <div class="cover__brand">8Fennox</div>
  <div class="display cover__label">Our Vision</div>
  <div class="display cover__line1">Redefine</div>
  <div class="display cover__line2">The</div>
  <div class="display cover__line3">Consulting E<span class="slash-x">X</span>perience</div>
  <footer class="footer">
    <div class="footer__top"><span>©COPYRIGHT 2015 8Fennox</span><span>|</span><span>CONFIDENTIAL</span><span>|</span><span>www.8fennox.com</span></div>
    <div class="footer__name">8Fennox</div>
    <div class="footer__bottom"><span>Clear Practical Insights</span><span>|</span><span>Focused Solutions</span></div>
  </footer>
</section>

<section class="page page--inside">
  <svg class="page__shapes" viewBox="0 0 580 400" aria-hidden="true">
    <polygon points="0,30 580,0 580,44 0,70" fill="var(--charcoal)"/>
    <polygon points="0,70 580,44 580,96 330,100 0,88" fill="var(--red)"/>
    <rect x="0" y="344" width="580" height="26" fill="var(--slate)"/>
  </svg>
  <h1 class="display inside__title">Why We Are Different?</h1>
  <p class="inside__sub">"What is the secret sauce?<br>How did you achieve the impossible?"</p>

  <div class="cards">
    <article class="card">
      <svg class="card__icon" viewBox="0 0 20 20" aria-hidden="true"><circle cx="10" cy="4" r="3" fill="var(--red)"/><rect x="9" y="7" width="2" height="5" fill="var(--red)"/><rect x="3" y="11" width="14" height="2" fill="var(--red)"/><circle cx="4" cy="16" r="2.5" fill="var(--red)"/><circle cx="16" cy="16" r="2.5" fill="var(--red)"/></svg>
      <div class="card__box">
        <svg class="card__corner" viewBox="0 0 40 34" aria-hidden="true"><polygon points="0,0 40,0 0,34" fill="var(--red)"/></svg>
        <h2 class="card__title">Partnership with IT &amp; Business</h2>
        <p class="card__text">Relationships anchored in your culture, understanding your everyday challenges.</p>
        <p class="card__text">Connecting teams at all levels with business and technology, working to remove barriers.</p>
      </div>
    </article>
    <article class="card">
      <svg class="card__icon" viewBox="0 0 20 20" aria-hidden="true"><circle cx="8" cy="8" r="5.5" fill="none" stroke="var(--red)" stroke-width="2.4"/><line x1="12" y1="12" x2="18" y2="18" stroke="var(--red)" stroke-width="3" stroke-linecap="round"/></svg>
      <div class="card__box">
        <svg class="card__corner" viewBox="0 0 40 34" aria-hidden="true"><polygon points="0,0 40,0 0,34" fill="var(--red)"/></svg>
        <h2 class="card__title">Our People</h2>
        <p class="card__text">We have handpicked some of the best and brightest minds in the field.</p>
        <p class="card__text">Our project leaders are reliable, move quickly and stay in the details.</p>
      </div>
    </article>
    <article class="card">
      <svg class="card__icon" viewBox="0 0 20 20" aria-hidden="true"><rect x="7" y="2" width="6" height="4" fill="none" stroke="var(--red)" stroke-width="2"/><rect x="1" y="6" width="18" height="12" rx="1.5" fill="var(--red)"/><rect x="8" y="10" width="4" height="3" fill="var(--paper)"/></svg>
      <div class="card__box">
        <svg class="card__corner" viewBox="0 0 40 34" aria-hidden="true"><polygon points="0,0 40,0 0,34" fill="var(--red)"/></svg>
        <h2 class="card__title">Prepared</h2>
        <p class="card__text">Refining all the processes, templates and tools needed to plan projects with clarity.</p>
        <p class="card__text">Our experience tells us what we need to know before we begin.</p>
      </div>
    </article>
    <article class="card">
      <svg class="card__icon" viewBox="0 0 20 20" aria-hidden="true"><path d="M4 10a6 6 0 0 1 10-4.5" fill="none" stroke="var(--red)" stroke-width="2.6"/><polygon points="16,2 16,8 10,7" fill="var(--red)"/><path d="M16 10a6 6 0 0 1-10 4.5" fill="none" stroke="var(--red)" stroke-width="2.6"/><polygon points="4,18 4,12 10,13" fill="var(--red)"/></svg>
      <div class="card__box">
        <svg class="card__corner" viewBox="0 0 40 34" aria-hidden="true"><polygon points="0,0 40,0 0,34" fill="var(--red)"/></svg>
        <h2 class="card__title">Flexible</h2>
        <p class="card__text">Firm preparation creates adaptability; plans can absorb unplanned challenges.</p>
        <p class="card__text">Being nimble enough to change direction keeps delivery on track.</p>
      </div>
    </article>
    <article class="card">
      <svg class="card__icon" viewBox="0 0 20 20" aria-hidden="true"><rect x="8" y="0" width="4" height="3" fill="var(--red)"/><circle cx="10" cy="11.5" r="7" fill="none" stroke="var(--red)" stroke-width="2.4"/><line x1="10" y1="11.5" x2="10" y2="7" stroke="var(--red)" stroke-width="2"/></svg>
      <div class="card__box">
        <svg class="card__corner" viewBox="0 0 40 34" aria-hidden="true"><polygon points="0,0 40,0 0,34" fill="var(--red)"/></svg>
        <h2 class="card__title">Pace &amp; Energy</h2>
        <p class="card__text">We bring focused and high-energy effort to all of our projects.</p>
        <p class="card__text">Our pace and momentum will steadily outpace the rest.</p>
      </div>
    </article>
  </div>

  <footer class="footer">
    <div class="footer__top"><span>©COPYRIGHT 2015 8Fennox</span><span>|</span><span>CONFIDENTIAL</span><span>|</span><span>www.8fennox.com</span></div>
    <div class="footer__name">8Fennox</div>
    <div class="footer__bottom"><span>Clear Practical Insights</span><span>|</span><span>Focused Solutions</span></div>
  </footer>
</section>

</body>
</html>
```